Trailer wrap

Looking for a trailer wrap. I have attached a file of my logo. Also use the phone number 555-201-3846. integrate one or both of the following slogans - ""Solutions You Can Trust" - ""Prompt. Able. Neat. Kind. That’s the PANK Difference" If possible integrate a United States flag, possibly in grayscale. The following are my colors: Orange F16A21 Blue 4D91D9.

```html
<!DOCTYPE html>
<html lang="en">
<head>
<meta charset="utf-8">
<title>PANK HVAC &amp; Plumbing – Trailer Wrap</title>
<link rel="stylesheet" href="https://fonts.googleapis.com/css2?family=Anton&family=Open+Sans:wght@700&family=Roboto+Condensed:wght@700&display=swap">
<style>
  :root {
    --orange: #F16A21;
    --orange-light: #F7932B;
    --blue: #4D91D9;
    --blue-deep: #1E88D6;
    --navy: #2A2C9E;
    --red: #E3262B;
    --yellow: #FFE100;
    --white: #FFFFFF;
    --backdrop: #ECEDEF;
  }
  html, body {
    margin: 0;
    padding: 0;
    width: 1200px;
    height: 904px;
    overflow: hidden;
    background: var(--backdrop);
  }
  .canvas {
    position: relative;
    width: 1200px;
    height: 904px;
  }
  .wrap-panel {
    position: absolute;
    left: 20px;
    top: 197px;
    width: 1160px;
    height: 510px;
    background: var(--white);
    border-radius: 10px 10px 2px 2px;
    overflow: hidden;
    box-shadow: 0 2px 8px rgba(0,0,0,0.12);
  }
  .wrap-panel svg.graphics {
    position: absolute;
    inset: 0;
  }
  .brand-name {
    position: absolute;
    font-family: "Anton", sans-serif;
    color: var(--orange);
    letter-spacing: 0.22em;
    line-height: 1;
    white-space: nowrap;
  }
  .brand-name--main {
    left: 196px;
    top: 120px;
    font-size: 96px;
  }
  .brand-name--front {
    left: 14px;
    top: 92px;
    font-size: 26px;
    letter-spacing: 0.18em;
  }
  .brand-mark {
    position: absolute;
    border-radius: 50%;
    background: var(--blue);
  }
  .brand-mark--main {
    left: 338px;
    top: 60px;
    width: 42px;
    height: 42px;
  }
  .brand-mark--front {
    left: 46px;
    top: 72px;
    width: 14px;
    height: 14px;
  }
  .headline {
    position: absolute;
    font-family: "Anton", sans-serif;
    line-height: 1;
    white-space: nowrap;
    transform-origin: left bottom;
    -webkit-background-clip: text;
    background-clip: text;
    color: transparent;
    filter: drop-shadow(2px 2px 0 var(--white)) drop-shadow(-2px -2px 0 var(--white)) drop-shadow(2px -2px 0 var(--white)) drop-shadow(-2px 2px 0 var(--white)) drop-shadow(3px 4px 2px rgba(0,0,0,0.25));
  }
  .headline--trade {
    left: 615px;
    top: 60px;
    font-size: 100px;
    transform: rotate(-14deg);
    background-image: linear-gradient(180deg, var(--red) 10%, var(--orange) 45%, var(--yellow) 90%);
  }
  .headline--service {
    left: 735px;
    top: 148px;
    font-size: 82px;
    transform: rotate(-14deg);
    background-image: linear-gradient(180deg, var(--blue-deep) 0%, var(--blue) 45%, var(--navy) 100%);
  }
  .slogan {
    position: absolute;
    left: 240px;
    top: 408px;
    font-family: "Open Sans", sans-serif;
    font-weight: 700;
    font-size: 26px;
    line-height: 40px;
    color: var(--white);
    letter-spacing: 0.02em;
    white-space: nowrap;
    transform: rotate(-15deg);
    transform-origin: left bottom;
  }
  .phone {
    position: absolute;
    left: 668px;
    top: 290px;
    font-family: "Roboto Condensed", sans-serif;
    font-weight: 700;
    font-size: 54px;
    color: var(--white);
    white-space: nowrap;
    transform: rotate(-12.5deg) scaleY(1.15);
    transform-origin: left bottom;
  }
</style>
</head>
<body>
<div class="canvas">
  <section class="wrap-panel" aria-label="Trailer side wrap">
    <svg class="graphics" width="1160" height="510" viewBox="0 0 1160 510" aria-hidden="true">
      <defs>
        <linearGradient id="front-fade" x1="0" y1="0" x2="0" y2="1">
          <stop offset="0.35" stop-color="#FFFFFF"/>
          <stop offset="0.95" stop-color="#F16A21"/>
        </linearGradient>
        <linearGradient id="lower-fade" x1="0" y1="0" x2="0" y2="1">
          <stop offset="0.55" stop-color="#FFFFFF"/>
          <stop offset="0.85" stop-color="#F9B48A"/>
        </linearGradient>
      </defs>
      <!-- front end fade and body fade -->
      <rect class="front-end" x="0" y="0" width="108" height="510" fill="url(#front-fade)"/>
      <rect class="body-fade" x="108" y="0" width="1052" height="510" fill="url(#lower-fade)"/>
      <line x1="108" y1="0" x2="108" y2="510" stroke="#D7D7D7" stroke-width="1.5"/>
      <!-- orange lower band -->
      <polygon class="band-orange" points="108,430 1160,170 1160,510 108,510" fill="var(--orange)"/>
      <!-- light orange accent stroke -->
      <polygon class="band-accent" points="1050,220 1160,190 1160,215 1080,238 1040,320 880,350 1000,315" fill="var(--orange-light)"/>
      <!-- blue stripe -->
      <polygon class="band-blue" points="108,492 628,356 628,366 108,503" fill="var(--blue)"/>
      <!-- blue phone panel -->
      <polygon class="phone-panel" points="628,356 650,300 1040,205 1018,262" fill="var(--blue)"/>
      <polygon class="band-blue-upper" points="1040,205 1160,176 1160,186 1036,216" fill="var(--blue)"/>
    </svg>

    <span class="brand-mark brand-mark--front"></span>
    <span class="brand-name brand-name--front">PANK</span>

    <span class="brand-mark brand-mark--main"></span>
    <span class="brand-name brand-name--main">PANK</span>

    <div class="headline headline--trade">HVAC &amp;</div>
    <div class="headline headline--service">Plumbing</div>

    <div class="slogan">Solutions You Can Trust</div>
    <div class="phone">555-201-3846</div>
  </section>
</div>
</body>
</html>
```